3 JPG Website Page Mockups need tidying / made into layered PSDs

Our website is aimed at creating a financial eduction site for females.

We have mockups of each page which are provided in jpeg.... but they need to be tidied up, layered into PSD (with descriptive layer names to allow coding from and no flattening - each object needs it's own layer) and we welcome any creative improvements suggested (although we are pretty happy with the way it's laid out at the moment as it is), without changing the feel, colour scheme or functionality of the site.

Three pages are needed:
Home page when not logged in
Home page when logged in
Topic header page

Please just upload the homepage to bid for the job... the winning designer will then have 5 days after they've been chosen to supply the psds of the other 2 pages .

I have also uploaded an image that can be used as a placeholder in the top box.
Thanks
Updates

As requested... Current font is Gill Sans MT

Thanks

Hi
Thanks for your designs.... For those of you still using the 4 circles (which I quite like), but haven't yet done so, could you see if you can move them around slightly to that the words don't get covered by the next circle?

Thanks

Reason: Designe has asked for An extension to work on new icons... would like to give them the time to see what they come up with, thanks

Industry/Entity Type

Financial

Requirements
Must have
• Maintain current feel & colour scheme of the website

```html
<!DOCTYPE html>
<html lang="en">
<head>
<meta charset="utf-8">
<title>The Wealthwise Woman – Home</title>
<link rel="stylesheet" href="https://fonts.googleapis.com/css2?family=Cabin:wght@400;500;600;700&family=Fredoka:wght@500;600&family=Oswald:wght@500;600&display=swap">
<style>
:root{
  --teal:#1f9a9c;
  --teal-dark:#137a7d;
  --teal-light:#5ccfc6;
  --teal-mid:#35b2ad;
  --teal-ink:#17777b;
  --grey-bg:#d9d9d9;
  --grey-ink:#555;
  --orange:#f7941d;
  --orange-light:#f6ad55;
  --brown-ink:#3a2514;
  --white:#fff;
  --ink:#1d2d2d;
}
*{box-sizing:border-box;margin:0;padding:0}
html,body{width:1200px;height:900px;overflow:hidden;background:var(--white)}
body{position:relative;font-family:"Cabin",sans-serif}
.site{position:absolute;left:7px;top:93px;width:1185px;height:676px;border:1px solid #888}
.abs{position:absolute}

/* top navigation */
.main-nav{left:0;top:0;width:100%;height:27px;background:linear-gradient(#2bb0b1,var(--teal-dark));display:flex;align-items:center;color:var(--white);font-size:14px}
.main-nav a{position:absolute;top:0;height:27px;line-height:27px;color:inherit;text-decoration:none}
.main-nav .sep{position:absolute;top:3px;width:1px;height:21px;background:rgba(255,255,255,.55)}
.main-nav .active{background:linear-gradient(#f2f2f2,#a9a9a9);color:#333;text-align:center}
.region{position:absolute;left:1055px;top:6px;display:flex;align-items:center;gap:5px;font-size:11px}

/* header */
.header{left:0;top:27px;width:100%;height:154px;background:linear-gradient(#ececec,#d2d2d2)}
.brand-mark{left:110px;top:14px;display:flex;align-items:center;gap:6px;color:#8a8a8a;font-size:17px;font-weight:600}
.brand-mark i{display:block;width:26px;height:26px;border-radius:50%;background:#9a9a9a}
.welcome{left:81px;top:92px;color:var(--grey-ink);font-size:18px;font-weight:600;line-height:23px}
.search-title{left:358px;top:22px;width:420px;text-align:center;color:var(--teal-ink);font-size:22px;font-weight:700}
.search-box{left:358px;top:63px;width:428px;height:31px;border-radius:16px;background:var(--white);border:1px solid #c9c9c9;box-shadow:inset 0 1px 3px rgba(0,0,0,.15);font-size:14px;color:#333;padding:7px 16px}
.search-btn{position:absolute;right:7px;top:5px;width:20px;height:20px;border-radius:50%;background:var(--orange)}
.member-title{left:896px;top:22px;color:var(--teal-ink);font-size:22px;font-weight:700}
.member-links{left:896px;top:56px;font-size:12px;color:#333;list-style:none}
.member-links li{display:flex;align-items:center;gap:9px;height:27px}
.member-links b{display:inline-flex;width:18px;height:18px;border-radius:50%;background:var(--orange);color:#fff;font-size:12px;align-items:center;justify-content:center}
.member-links strong{font-weight:700}

/* sub navigation */
.sub-nav{left:0;top:181px;width:100%;height:28px;background:linear-gradient(#2db0b0,var(--teal-dark));color:var(--white);font-size:14px}
.sub-nav span{position:absolute;top:6px}
.sub-nav .sep{position:absolute;top:4px;width:1px;height:20px;background:rgba(255,255,255,.55)}

/* feature panel */
.feature{left:0;top:209px;width:509px;height:467px;background:linear-gradient(var(--teal-light),var(--teal-mid));border-right:1px solid #666}
.feature h2{position:absolute;left:27px;top:18px;font-family:"Fredoka",sans-serif;font-weight:600;font-size:22px;color:var(--ink)}
.tagline{position:absolute;left:27px;top:54px;color:var(--white);font-size:29px;line-height:37.5px;text-shadow:0 1px 2px rgba(0,0,0,.35)}
.video{position:absolute;left:228px;top:56px;width:256px;height:210px;background:#222}
.video-still{position:absolute;left:0;top:0;width:256px;height:192px;background:linear-gradient(120deg,#4a2f25,#7a5346 45%,#3a2a24)}
.play{position:absolute;left:108px;top:74px;width:40px;height:44px;background:rgba(40,40,40,.8)}
.caption{position:absolute;left:0;top:138px;width:152px;height:42px;background:rgba(90,140,100,.85);color:#fff;padding:3px 8px;font-family:"Oswald",sans-serif}
.caption b{display:block;font-size:14px;letter-spacing:1px;font-weight:500}
.caption small{display:block;font-size:7.5px;line-height:9px;letter-spacing:.4px}
.controls{position:absolute;left:0;top:192px;width:256px;height:18px;background:linear-gradient(#f4f4f4,#cfcfcf);font-size:7px;color:#666}
.controls span{position:absolute;top:5px}
.bubble{position:absolute;top:284px;width:128px;height:128px;border-radius:50%;text-align:center;color:#fff}
.bubble .cta{position:absolute;left:0;width:100%;font-size:11px}
.bubble-guide{left:10px;background:radial-gradient(circle at 40% 30%,#ff7b7b,#e22a2a 60%,#b31515)}
.bubble-poll{left:130px;background:radial-gradient(circle at 40% 30%,#8fb0ff,#3b6fd6 60%,#2a4fa5)}
.bubble-stories{left:251px;background:radial-gradient(circle at 40% 30%,#fff36a,#e7c21e 60%,#c59a10)}
.bubble-ask{left:372px;background:radial-gradient(circle at 40% 30%,#f07cf5,#c02fd6 60%,#8e17b0)}
.bubble .head{position:absolute;left:0;width:100%;font-family:"Oswald",sans-serif;font-weight:600;line-height:24px}
.bubble-guide .head{top:36px;font-size:20px;color:#f5e08a;text-shadow:0 1px 2px #6a1a00}
.bubble-poll .head{top:60px;font-size:16px;color:#f6ec4a}
.bubble-stories .head{top:36px;font-size:18px;color:#6a4a10}
.bubble-ask .q{position:absolute;left:16px;top:22px;width:100px;text-align:left;font-size:10.5px;line-height:14px;color:#111;font-weight:600}
.reflection{position:absolute;top:412px;height:18px;width:120px;border-radius:50%;background:rgba(0,60,60,.18)}
.feature-foot{position:absolute;left:0;bottom:0;width:100%;height:20px;background:#6fd3ca;font-size:11px;font-weight:700;color:#1b3333;padding:3px 31px}

/* promo panel */
.promo{left:509px;top:209px;width:439px;height:467px;background:var(--orange);border-right:1px solid #666}
.promo h1{position:absolute;left:50px;top:26px;width:350px;color:var(--brown-ink);font-size:20px;line-height:28px;font-weight:600}
.promo-photo{position:absolute;left:0;top:128px;width:439px;height:319px;background:linear-gradient(180deg,#f29a30 0%,#e9d8c6 55%,#8a4a26 100%)}
.promo-foot{position:absolute;left:0;bottom:0;width:100%;height:20px;background:var(--orange-light);font-size:11px;font-weight:700;color:var(--brown-ink)}
.promo-foot .join{position:absolute;left:49px;top:3px}
.pager{position:absolute;right:46px;top:3px;letter-spacing:3px}

/* topic menu */
.topic-menu{left:948px;top:209px;width:236px;height:467px;list-style:none}
.topic-menu li{position:relative;height:58.4px;background:linear-gradient(#8ae0d9,#3db8b1);border-bottom:1px solid #2a8f8a;color:#fff;font-size:15px;font-weight:700;text-shadow:0 1px 2px rgba(0,0,0,.45)}
.topic-menu .icon{position:absolute;left:21px;top:11px;width:36px;height:36px;border:2px solid #fff;border-radius:4px;background:#2f9d98}
.topic-menu span{position:absolute;left:74px;top:19px}
.cursor{left:280px;top:108px}
</style>
</head>
<body>
<div class="site">

  <nav class="abs main-nav">
    <a style="left:18px">Home</a><i class="sep" style="left:76px"></i>
    <a style="left:115px">Polls</a><i class="sep" style="left:181px"></i>
    <a class="active" style="left:182px;width:107px">Events</a>
    <i class="sep" style="left:290px"></i>
    <a style="left:324px">Learning Centre</a><i class="sep" style="left:455px"></i>
    <a style="left:490px">Find an Adviser</a><i class="sep" style="left:615px"></i>
    <a style="left:649px">Ask a Question</a><i class="sep" style="left:771px"></i>
    <a style="left:804px">About Us</a>
    <div class="region">
      <svg width="24" height="14" viewBox="0 0 24 14"><rect width="24" height="14" fill="#1c2f7a"/><rect width="10" height="7" fill="#b22"/><path d="M0 3.5H10M5 0V7" stroke="#fff" stroke-width="1.5"/><circle cx="17" cy="9" r="1.3" fill="#fff"/><circle cx="20" cy="4" r="1" fill="#fff"/></svg>
      <span>AU ▾</span>
    </div>
  </nav>

  <header class="abs header">
    <div class="abs brand-mark"><i></i>Company Logo</div>
    <p class="abs welcome">Welcome to the new<br>Wealthwise Woman Site</p>
    <h2 class="abs search-title">What are &nbsp;you looking for?</h2>
    <div class="abs search-box">Search The Wealthwise Woman for......
      <span class="search-btn"><svg width="20" height="20" viewBox="0 0 20 20"><circle cx="9" cy="9" r="4" fill="none" stroke="#fff" stroke-width="1.8"/><path d="M12 12l3 3" stroke="#fff" stroke-width="2"/></svg></span>
    </div>
    <h2 class="abs member-title">Already a member?</h2>
    <ul class="abs member-links">
      <li><b>+</b>Login</li>
      <li><b>▸</b>Forgotten Password</li>
      <li><b>?</b>Not yet a member? <strong>Register here &gt;</strong></li>
    </ul>
  </header>

  <nav class="abs sub-nav">
    <span style="left:29px">Popular Searches</span><i class="sep" style="left:155px"></i>
    <span style="left:175px">Explore the Learning Centre</span><i class="sep" style="left:367px"></i>
    <span style="left:389px">Ask A Question</span>
  </nav>

  <section class="abs feature">
    <h2>July Topic: Preparing for Retirement</h2>
    <p class="tagline">Tomorrow<br>Can Belong<br>to Those Who<br>Prepare Today</p>
    <div class="video">
      <div class="video-still" role="img" aria-label="Video still of the founder speaking in her office"></div>
      <div class="play"><svg width="40" height="44" viewBox="0 0 40 44"><path d="M14 13l14 9-14 9z" fill="#fff"/></svg></div>
      <div class="caption"><b>DANA WHITLOCK</b><small>FOUNDER, CHAIRMAN &amp; CEO<br>HARBOUR &amp; CO.</small></div>
      <div class="controls"><span style="left:5px">▶ ■</span><span style="left:36px">00:00</span><span style="left:170px">00:00</span><span style="left:214px">⛶ ◂)</span></div>
    </div>

    <div class="bubble bubble-guide"><div class="head">5 Minute<br>GUIDE</div><div class="cta" style="top:90px">PDF &gt;</div></div>
    <div class="bubble bubble-poll">
      <svg class="abs" style="left:12px;top:18px" width="104" height="42" viewBox="0 0 104 42">
        <g fill="#2a3fc9" stroke="#9fc0ff" stroke-width="1">
          <rect x="2" y="30" width="8" height="12"/><rect x="13" y="24" width="8" height="18"/><rect x="24" y="28" width="8" height="14"/><rect x="35" y="10" width="8" height="32"/><rect x="46" y="2" width="8" height="40"/><rect x="57" y="14" width="8" height="28"/><rect x="68" y="20" width="8" height="22"/><rect x="79" y="26" width="8" height="16"/><rect x="90" y="18" width="8" height="24"/>
        </g>
      </svg>
      <div class="head">Take our Poll</div><div class="cta" style="top:90px">Vote &gt;</div>
    </div>
    <div class="bubble bubble-stories"><div class="head">REAL WOMEN<br>REAL STORIES</div><div class="cta" style="top:92px">See Video &gt;</div></div>
    <div class="bubble bubble-ask"><p class="q">Have questions about Life stages &amp; Planning? Ask a question or see what others have asked... <span style="color:#fff;font-weight:400">More &gt;</span></p></div>
    <i class="reflection" style="left:14px"></i><i class="reflection" style="left:134px"></i><i class="reflection" style="left:255px"></i><i class="reflection" style="left:376px"></i>
    <div class="feature-foot">Learn More &gt;</div>
  </section>

  <section class="abs promo">
    <h1>We’re building Australia’s biggest community dedicated to the Financial Empowerment of Women.</h1>
    <div class="promo-photo" role="img" aria-label="Photo of two women chatting over coffee at a table"></div>
    <div class="promo-foot"><span class="join">Join Now for FREE &gt;</span><span class="pager">&lt; 1 2 3 4 &gt;</span></div>
  </section>

  <ul class="abs topic-menu">
    <li><svg class="icon" viewBox="0 0 36 36"><path d="M8 10h20v12H16l-5 5v-5H8z" fill="none" stroke="#fff" stroke-width="2"/></svg><span>Welcome</span></li>
    <li><svg class="icon" viewBox="0 0 36 36"><path d="M7 27h22M9 27v-5h4v5M14 27v-8h4v8M19 27v-11h4v11M24 27v-14h4v14" fill="none" stroke="#fff" stroke-width="1.6"/></svg><span>Events</span></li>
    <li><svg class="icon" viewBox="0 0 36 36"><g fill="none" stroke="#fff" stroke-width="2"><path d="M7 15a16 16 0 0 1 22 0"/><path d="M11 19a10 10 0 0 1 14 0"/><path d="M15 23a4 4 0 0 1 6 0"/></g><circle cx="18" cy="27" r="1.8" fill="#fff"/></svg><span>Webcasts</span></li>
    <li><svg class="icon" viewBox="0 0 36 36"><g fill="#fff"><circle cx="11" cy="10" r="3"/><circle cx="25" cy="10" r="3"/><circle cx="18" cy="17" r="2"/><rect x="8" y="14" width="6" height="14"/><rect x="22" y="14" width="6" height="14"/><rect x="16.5" y="20" width="3" height="8"/></g></svg><span>My Family</span></li>
    <li><svg class="icon" viewBox="0 0 36 36"><path d="M7 7v22h22M10 25l6-7 4 4 8-10" fill="none" stroke="#fff" stroke-width="2"/></svg><span>My Investments</span></li>
    <li><svg class="icon" viewBox="0 0 36 36"><path d="M6 17a12 9 0 0 1 24 0zM18 17v8M6 28c4-3 8 3 12 0s8 3 12 0" fill="none" stroke="#fff" stroke-width="2"/></svg><span>My Retirement</span></li>
    <li><svg class="icon" viewBox="0 0 36 36"><path d="M6 18L18 7l12 11M10 15v13h16V15M15 28v-7h6v7" fill="none" stroke="#fff" stroke-width="2"/></svg><span>My Estate</span></li>
    <li><svg class="icon" viewBox="0 0 36 36"><circle cx="18" cy="9" r="3" fill="#fff"/><path d="M18 13v8M10 19l8-4 8 4M8 27h20M11 26l7-4 7 4" fill="none" stroke="#fff" stroke-width="2"/></svg><span>My Lifestyle</span></li>
  </ul>
</div>

<svg class="abs cursor" width="18" height="26" viewBox="0 0 18 26"><path d="M1 1v19l5-5 4 9 3-1-4-9h7z" fill="#fff" stroke="#000" stroke-width="1.2"/></svg>
</body>
</html>
```